Stationary or Corporate Identity package for small Software Development Company

I have a logo and am looking for letterhead, envelope, and possibly business card design. Letterhead and envelope can use all images from the attached business card or open to other ideas that can incorporate the logo. Looking for colorful design to grab attention. Also wanting a more Professional look and less whimsical with maybe a little on the bolder side (maybe more of the masculine side?) Definitely a more modern look over a boring traditional look.

Target Market(s)

Clients are IT Recruiters and IT/Software Staffing and Consulting companies

Industry/Entity Type

Computer Software

Font styles to use
Sans Serif

Requirements
Must have
• Must have the logo, and places for address information, phone number, email, and website information. Colors should coordinate with logo.
Nice to have
• I like the look where there is a semi-transparent abstract image or part of the logo that sort of swooshes in from the left side of the paper. This is not necessary if other good ideas come to mind. Would like a little bit of color to the stationary and envelope, not just a header/footer type with just the logo and a colored separation line.

```html
<!DOCTYPE html>
<html lang="en">
<head>
<meta charset="UTF-8">
<title>Veltrix Envelope Set</title>
<link href="https://fonts.googleapis.com/css2?family=Open+Sans:wght@400;700&display=swap" rel="stylesheet">
<style>
  :root {
    --stage: #5aaef0;
    --navy: #17304a;
    --navy-deep: #12263b;
    --glow: #2588d0;
    --band: #3b6fc2;
    --band-dark: #2c56a3;
    --lime: #6cc22a;
    --paper: #ededed;
    --paper-edge: #d6d6d6;
    --flap: #2f63b8;
    --ink: #141414;
    --accent: #e8562a;
  }
  * { margin: 0; padding: 0; box-sizing: border-box; }
  html, body { width: 1200px; height: 950px; overflow: hidden; }
  body {
    background: var(--stage);
    font-family: "Open Sans", sans-serif;
    position: relative;
  }
  .envelope { position: absolute; width: 820px; height: 390px; overflow: hidden; }
  .envelope--front { left: 60px; top: 45px; }
  .envelope--back { left: 320px; top: 505px; background: var(--paper); border: 1px solid var(--paper-edge); }
  .envelope__art { position: absolute; inset: 0; display: block; width: 100%; height: 100%; }

  .brand { position: absolute; display: flex; align-items: center; gap: 12px; }
  .brand__dot { border-radius: 50%; background: var(--accent); flex: none; }
  .brand__name { font-weight: 700; line-height: 1; }
  .brand__tag { font-weight: 400; line-height: 1.2; }

  .envelope--front .brand { left: 40px; top: 175px; color: #fff; }
  .envelope--front .brand__dot { width: 54px; height: 54px; }
  .envelope--front .brand__name { font-size: 38px; }
  .envelope--front .brand__tag { font-size: 14px; opacity: .85; }

  .envelope--back .brand { left: 520px; top: 250px; color: var(--ink); }
  .envelope--back .brand__dot { width: 40px; height: 40px; }
  .envelope--back .brand__name { font-size: 28px; }
  .envelope--back .brand__tag { font-size: 10px; }

  .contact {
    position: absolute; right: 30px; top: 290px;
    color: #fff; font-size: 11.5px; line-height: 1.9;
  }
  .contact__row { display: flex; justify-content: flex-end; align-items: center; gap: 6px; white-space: nowrap; }
  .contact__icon { display: block; width: 11px; height: 11px; flex: none; }
  .contact__sep { width: 10px; flex: none; }
</style>
</head>
<body>

  <section class="envelope envelope--front" aria-label="Envelope front">
    <svg class="envelope__art" viewBox="0 0 820 390" preserveAspectRatio="none">
      <defs>
        <radialGradient id="frontGlow" cx="0.5" cy="0.5" r="0.55">
          <stop offset="0" stop-color="#2588d0"/>
          <stop offset="0.55" stop-color="#1d4e78"/>
          <stop offset="1" stop-color="#17304a"/>
        </radialGradient>
        <linearGradient id="bandFill" x1="0" y1="0" x2="0" y2="1">
          <stop offset="0" stop-color="#3b6fc2"/>
          <stop offset="1" stop-color="#4b82cc"/>
        </linearGradient>
      </defs>
      <rect width="820" height="390" fill="#12263b"/>
      <rect role="img" aria-label="Soft blue light streaks across the envelope" x="0" y="0" width="820" height="390" fill="url(#frontGlow)"/>
      <rect x="560" y="30" width="230" height="125" rx="22" fill="#f2f2f2"/>
      <path d="M0,300 C210,390 400,330 560,240 S740,170 820,165 V390 H0 Z" fill="#2c56a3"/>
      <path d="M0,318 C230,405 430,335 580,255 S760,185 820,182" fill="none" stroke="#6cc22a" stroke-width="6"/>
      <path d="M0,326 C230,413 430,343 580,263 S760,193 820,190 V390 H0 Z" fill="url(#bandFill)"/>
      <rect x="0" y="150" width="6" height="45" fill="#6cc22a"/>
      <rect x="0" y="198" width="6" height="60" fill="#3b6fc2"/>
    </svg>

    <div class="brand">
      <span class="brand__dot"></span>
      <div>
        <div class="brand__name">Veltrix</div>
        <div class="brand__tag">Software Development</div>
      </div>
    </div>

    <div class="contact">
      <div class="contact__row">
        <svg class="contact__icon" viewBox="0 0 12 12"><circle cx="6" cy="6" r="6" fill="#6cc22a"/><path d="M6 2.5a2.3 2.3 0 0 0-2.3 2.3C3.7 6.6 6 9.5 6 9.5s2.3-2.9 2.3-4.7A2.3 2.3 0 0 0 6 2.5z" fill="#fff"/></svg>
        <span>12 Sample Road, Market Row, 000 UK</span>
      </div>
      <div class="contact__row">
        <svg class="contact__icon" viewBox="0 0 12 12"><rect width="12" height="12" rx="2" fill="#6cc22a"/><path d="M3.5 2.5h1.5l.7 1.8-1 .7a5 5 0 0 0 2.3 2.3l.7-1 1.8.7v1.5A1 1 0 0 1 8.5 9.5 6 6 0 0 1 2.5 3.5a1 1 0 0 1 1-1z" fill="#fff"/></svg>
        <span>+02 004 118 2260</span>
        <span class="contact__sep"></span>
        <svg class="contact__icon" viewBox="0 0 12 12"><rect width="12" height="12" rx="2" fill="#6cc22a"/><rect x="2.5" y="3.5" width="7" height="5" fill="none" stroke="#fff"/><path d="M2.5 3.5 6 6.3 9.5 3.5" fill="none" stroke="#fff"/></svg>
        <span>hello@veltrix.com</span>
        <span class="contact__sep"></span>
        <svg class="contact__icon" viewBox="0 0 12 12"><circle cx="6" cy="6" r="6" fill="#6cc22a"/></svg>
        <span>www.veltrix.com</span>
      </div>
    </div>
  </section>

  <section class="envelope envelope--back" aria-label="Envelope back">
    <svg class="envelope__art" viewBox="0 0 820 390" preserveAspectRatio="none">
      <path d="M60,110 L20,385 M760,110 L800,385" stroke="#dcdcdc" stroke-width="1.5" fill="none"/>
      <path role="img" aria-label="Blue flap with interlocking geometric pattern" d="M0,0 H820 V70 Q820,80 810,84 L760,112 Q752,116 740,116 H80 Q68,116 60,112 L10,84 Q0,80 0,70 Z" fill="#2f63b8"/>
    </svg>
    <div class="brand">
      <span class="brand__dot"></span>
      <div>
        <div class="brand__name">Veltrix</div>
        <div class="brand__tag">Software Development</div>
      </div>
    </div>
  </section>

</body>
</html>
```